International MultiIndustry Team Coaching Site

Hello Designers,
We need a redesign of the pages attached.
The design must be engaging and modern, with a focus on the user experience, particularly for the "observations" page. Because this is the main page of the website. It is to be used on a 10'' tablet or desktop, to record observations on the fly, so it must be intuitive and efficient.
The positioning of the metrics and observations and etc, are just a reference. you can switch it up if you feel there is a better way (PLEASE DO ;) ).

There are many categories (color coded with borders in the example hpt_6_observations.jpg) and observation metrics within each category. This is the Key page, because it is the One with the most interactions.

The user should know when it has selected a category (there should be some visual hint) and the different metric widgets should be accounted for.
There are 3: The time widget at the end, numerical widgets (recording more or less numbers), and boolean ones (selected or not).

For the numerical widgets, we show plus and minus characters, but you can change this, being creative, keeping in mind that it must work well on a mobile device and desktop, and must be intuitive and quick.

Set your creativity free with the login screen , home screen, categories secret, events screen, journaling and observations screen .

We would like the site/mobile version to have a very modern look. Something that would be found in very popular and user friendly apps.

***** The events, journaling, category and home screens are getting 2 much attention , please focus also on the observations screen *******
Imagine you are a psychologist tasked with observing the behaviour of teenagers during group work. And you have a tablet on which to record what you observe. Now imagine you need to observe during 3 classes: Biology, Math, Physics (these are events). For each class (event) you will have to record observations in 3 categories: Social Interaction, Leadership, Communication (these are categories).
Example of the metrics (these are observations) for Leadership:
" the teenager direct other colleagues" (boolean widget),
"the teenager speaks more than everyone else" (boolean widget)
"the teenager interrupts colleagues speaking" (number widget)
"the work took hh:mm" (time widget)

The observations screen can have any shape and form you think of. It doesn't need to be that single column with yes and nos, or that double column with the squared cards.
thank you.

Hope that was useful intel :)
Available for any questions you might have.
Good luck :)

Enterprise teams

5+ page

Sans Serif

• Modern design

```html
<!DOCTYPE html>
<html lang="en">
<head>
<meta charset="utf-8">
<title>Grass Team – Events</title>
<link href="https://fonts.googleapis.com/css2?family=Poppins:wght@400;500;600&display=swap" rel="stylesheet">
<style>
:root{
  --bg:#f7f7f8;
  --white:#ffffff;
  --ink:#1c1c1c;
  --body:#5a5a5a;
  --muted:#777;
  --accent:#b3406c;
  --blue:#3d74c4;
  --line:#d9d9d9;
  --pager:#8c8c8c;
}
*{box-sizing:border-box;margin:0;padding:0}
html,body{width:1200px;height:862px;overflow:hidden}
body{font-family:'Poppins',sans-serif;background:var(--bg);color:var(--ink);position:relative}
.topbar{position:absolute;left:0;top:0;width:1200px;height:82px;background:var(--white);box-shadow:0 2px 8px rgba(0,0,0,.05)}
.brand{position:absolute;left:48px;top:33px;display:flex;align-items:center;gap:7px;font-size:15px;font-weight:600;color:var(--blue)}
.brand-dot{width:12px;height:12px;border-radius:50%;background:var(--blue)}
.search{position:absolute;left:177px;top:23px;width:313px;height:42px;border:1px solid #8a8a8a;border-radius:21px;display:flex;align-items:center;padding-left:15px;gap:12px;color:#8a8a8a;font-size:13px}
.tools{position:absolute;left:810px;top:34px;display:flex;gap:17px;align-items:center}
.tools svg{width:16px;height:16px}
.flag{width:21px;height:13px;background:linear-gradient(#203a8f,#203a8f);position:relative;overflow:hidden}
.bell{position:relative}
.badge{position:absolute;left:8px;top:-9px;width:13px;height:13px;border-radius:50%;background:var(--accent);color:#fff;font-size:8px;text-align:center;line-height:13px}
.divider{position:absolute;left:997px;top:5px;width:1px;height:77px;background:#cfcfcf}
.user{position:absolute;left:1017px;top:30px;display:flex;align-items:center;gap:10px;font-size:13px}
.avatar{width:35px;height:35px;border-radius:50%;background:linear-gradient(135deg,#8c9a86,#c9b6a0)}
.user b{color:var(--accent);font-weight:500}
.sidebar{position:absolute;left:0;top:82px;width:163px;height:608px;background:var(--white);box-shadow:2px 0 8px rgba(0,0,0,.04)}
.nav{list-style:none;position:absolute;left:14px;top:36px}
.nav li{display:flex;align-items:center;gap:9px;height:26.4px;font-size:11.5px;color:#333}
.nav li.active{color:var(--blue)}
.nav svg{width:13px;height:13px}
.page-title{position:absolute;left:177px;top:89px;font-size:16px;font-weight:600}
.panel{position:absolute;left:171px;top:123px;width:1001px;height:731px;background:var(--white);box-shadow:0 0 10px rgba(0,0,0,.05)}
.card{position:absolute;width:210px;height:290px;background:var(--white);box-shadow:0 1px 8px rgba(0,0,0,.08)}
.card-media{height:159px}
.card-title{margin:11px 0 0 17px;font-size:14px;font-weight:500;color:var(--accent)}
.card-text{margin:5px 14px 0 17px;font-size:8.8px;line-height:17.5px;color:var(--body)}
.card-btn{position:absolute;left:15px;top:249px;width:108px;height:24px;border:1.5px solid var(--blue);border-radius:12px;color:var(--blue);font-size:8.5px;font-weight:500;text-align:center;line-height:21px;background:none}
.pager{position:absolute;left:960px;top:780px;display:flex;align-items:center;gap:11px;font-size:14px;font-weight:500;color:var(--pager)}
.pager-btn{width:31px;height:31px;border-radius:50%;background:var(--pager);display:flex;align-items:center;justify-content:center}
</style>
</head>
<body>
<header class="topbar">
  <div class="brand"><span class="brand-dot"></span>Teamwise</div>
  <div class="search">
    <svg width="18" height="18" viewBox="0 0 20 20" fill="none" stroke="#333" stroke-width="2"><circle cx="8.5" cy="8.5" r="6.5"/><path d="M13.5 13.5 18 18"/></svg>
    Enter Keyword
  </div>
  <div class="tools">
    <svg viewBox="0 0 21 13" style="width:21px;height:13px"><rect width="21" height="13" fill="#1f3d8f"/><path d="M0 0 21 13M21 0 0 13" stroke="#fff" stroke-width="3"/><path d="M0 0 21 13M21 0 0 13" stroke="#c8102e" stroke-width="1"/><path d="M10.5 0v13M0 6.5h21" stroke="#fff" stroke-width="4"/><path d="M10.5 0v13M0 6.5h21" stroke="#c8102e" stroke-width="2"/></svg>
    <svg viewBox="0 0 16 16" fill="none" stroke="#555"><rect x="1.5" y="3" width="13" height="11.5" rx="1"/><path d="M1.5 6.5h13M5 1v3M11 1v3"/></svg>
    <svg viewBox="0 0 16 16" fill="none" stroke="#555"><rect x="2" y="2" width="5" height="5"/><rect x="9" y="2" width="5" height="5"/><rect x="2" y="9" width="5" height="5"/><rect x="9" y="9" width="5" height="5"/></svg>
    <span class="bell"><svg viewBox="0 0 16 16" fill="#555"><path d="M8 1.5a4.5 4.5 0 0 0-4.5 4.5v4L2 12h12l-1.5-2V6A4.5 4.5 0 0 0 8 1.5zM6.3 13.3a1.7 1.7 0 0 0 3.4 0z"/></svg><span class="badge">5</span></span>
    <svg viewBox="0 0 16 16" fill="none" stroke="#555"><circle cx="8" cy="8" r="2.3"/><path d="M8 1.5l1.2 1.6 2-.4.6 1.9 1.9.6-.4 2L14.5 8l-1.2 1.2.4 2-1.9.6-.6 1.9-2-.4L8 14.5l-1.2-1.2-2 .4-.6-1.9-1.9-.6.4-2L1.5 8l1.2-1.2-.4-2 1.9-.6.6-1.9 2 .4z"/></svg>
  </div>
  <div class="divider"></div>
  <div class="user">
    <div class="avatar" role="img" aria-label="User profile photo"></div>
    <span>Welcome <b>Ardent</b></span>
    <svg width="12" height="8" viewBox="0 0 12 8" fill="none" stroke="#222" stroke-width="1.5"><path d="M1 1.5l5 5 5-5"/></svg>
  </div>
</header>

<aside class="sidebar">
  <ul class="nav">
    <li><svg viewBox="0 0 14 14" fill="none" stroke="#444"><path d="M1.5 6.5 7 1.5l5.5 5M3 5.5V12.5h8V5.5"/></svg>Home</li>
    <li class="active"><svg viewBox="0 0 14 14" fill="none" stroke="#3d74c4"><rect x="1.5" y="2.5" width="11" height="10"/><path d="M1.5 5.5h11M4 8h1M7 8h1M10 8h1M4 10.5h1M7 10.5h1"/></svg>Event &amp; Listing</li>
    <li><svg viewBox="0 0 14 14" fill="none" stroke="#444"><rect x="1.5" y="1.5" width="4" height="4"/><rect x="8.5" y="1.5" width="4" height="4"/><rect x="1.5" y="8.5" width="4" height="4"/><rect x="8.5" y="8.5" width="4" height="4"/></svg>Category Listing</li>
    <li><svg viewBox="0 0 14 14" fill="none" stroke="#777"><rect x="2.5" y="1.5" width="9" height="11"/><path d="M4.5 4.5h5M4.5 7h5M4.5 9.5h3"/></svg>Observation Listing</li>
    <li><svg viewBox="0 0 14 14" fill="none" stroke="#777"><circle cx="7" cy="7" r="2.5"/><path d="M7 1v2M7 11v2M1 7h2M11 7h2M2.8 2.8l1.4 1.4M9.8 9.8l1.4 1.4M2.8 11.2l1.4-1.4M9.8 4.2l1.4-1.4"/></svg>Hpt Observations</li>
    <li><svg viewBox="0 0 14 14" fill="none" stroke="#999"><rect x="2" y="2" width="10" height="10"/><path d="M4 5h6M4 7h6M4 9h4"/></svg>Observations with...</li>
  </ul>
</aside>

<h1 class="page-title">Grass Team</h1>

<main class="panel">
  <article class="card" style="left:26px;top:30px"><div class="card-media" role="img" aria-label="Two colleagues planning with sticky notes on a wall" style="background:linear-gradient(120deg,#c9c2b0,#8e8a80 55%,#3b3f7a)"></div><h2 class="card-title">Grass Team</h2><p class="card-text">Lorem Ipsum is simply dummy text of the printing and typesetting industry. Lorem Ipsum has been</p><button class="card-btn">Add Observration</button></article>
  <article class="card" style="left:271px;top:30px"><div class="card-media" role="img" aria-label="Team meeting in a bright lounge" style="background:linear-gradient(120deg,#e2ddd4,#b9b0a2 60%,#8d8575)"></div><h2 class="card-title">Grass Team</h2><p class="card-text">Lorem Ipsum is simply dummy text of the printing and typesetting industry. Lorem Ipsum has been</p><button class="card-btn">Add Observration</button></article>
  <article class="card" style="left:517px;top:30px"><div class="card-media" role="img" aria-label="Rowing crew on rough sea" style="background:linear-gradient(160deg,#c7d3df,#7e95ad 55%,#52677f)"></div><h2 class="card-title">Grass Team</h2><p class="card-text">Lorem Ipsum is simply dummy text of the printing and typesetting industry. Lorem Ipsum has been</p><button class="card-btn">Add Observration</button></article>
  <article class="card" style="left:762px;top:30px"><div class="card-media" role="img" aria-label="Two colleagues planning with sticky notes on a wall" style="background:linear-gradient(120deg,#c9c2b0,#8e8a80 55%,#3b3f7a)"></div><h2 class="card-title">Grass Team</h2><p class="card-text">Lorem Ipsum is simply dummy text of the printing and typesetting industry. Lorem Ipsum has been</p><button class="card-btn">Add Observration</button></article>

  <article class="card" style="left:26px;top:344px"><div class="card-media" role="img" aria-label="Abstract connected pipes on white" style="background:linear-gradient(135deg,#f1f1f1,#c9cbcd)"></div><h2 class="card-title">Grass Team</h2><p class="card-text">Lorem Ipsum is simply dummy text of the printing and typesetting industry. Lorem Ipsum has been</p><button class="card-btn">Add Observration</button></article>
  <article class="card" style="left:271px;top:344px"><div class="card-media" role="img" aria-label="Two colleagues planning with sticky notes on a wall" style="background:linear-gradient(120deg,#c9c2b0,#8e8a80 55%,#3b3f7a)"></div><h2 class="card-title">Grass Team</h2><p class="card-text">Lorem Ipsum is simply dummy text of the printing and typesetting industry. Lorem Ipsum has been</p><button class="card-btn">Add Observration</button></article>
  <article class="card" style="left:517px;top:344px"><div class="card-media" role="img" aria-label="Abstract geometric blue facets" style="background:linear-gradient(150deg,#a9b8cc,#7f93ad 55%,#5d6f88)"></div><h2 class="card-title">Grass Team</h2><p class="card-text">Lorem Ipsum is simply dummy text of the printing and typesetting industry. Lorem Ipsum has been</p><button class="card-btn">Add Observration</button></article>
  <article class="card" style="left:762px;top:344px"><div class="card-media" role="img" aria-label="Team meeting in a bright lounge" style="background:linear-gradient(120deg,#e2ddd4,#b9b0a2 60%,#8d8575)"></div><h2 class="card-title">Grass Team</h2><p class="card-text">Lorem Ipsum is simply dummy text of the printing and typesetting industry. Lorem Ipsum has been</p><button class="card-btn">Add Observration</button></article>
</main>

<nav class="pager" aria-label="Pagination">
  <span class="pager-btn"><svg width="10" height="12" viewBox="0 0 10 12" fill="none" stroke="#fff" stroke-width="1.6"><path d="M7 1 2 6l5 5"/></svg></span>
  <span>1 to 7 pages</span>
  <span class="pager-btn" style="margin-left:11px"><svg width="10" height="12" viewBox="0 0 10 12" fill="none" stroke="#fff" stroke-width="1.6"><path d="M3 1l5 5-5 5"/></svg></span>
</nav>
</body>
</html>
```